Corwenna Foundation is a new grant making charity set up in the UK.

Having got a logo, we now need a website to go with it. We have worked out the text which people are going to need in order to then apply for grants. But having found out what we require they will probably need to go away and think about it.
We have to be careful of what images we use. So I have uploaded some images that we like. We are also going to be adding more pages almost immediately so need to think about the images for these.
I know basic wordpress so I will be able to add new pages/make alterations in future.
Updates
The website does need to be coded in Wordpress so that I can maintain it afterwards.
Corwenna
Brief changed to provide more money and we have also provided more possible pictures. And generally more explanation.
Target Market(s)
departments in universities, other charities doing work on relief of pain, people working in health service departments
Industry/Entity Type
Health Charity
Coding
Coded - Design and coding required
Number of Pages Required
4 page
Look and feel
Each slider illustrates characteristics of the customer's brand and the style your logo design should communicate.

```html
<!DOCTYPE html>
<html lang="en">
<head>
<meta charset="utf-8">
<title>Corwenna Foundation</title>
<link rel="stylesheet" href="https://fonts.googleapis.com/css2?family=Poppins:wght@300;400;500;600&family=Rajdhani:wght@500;700&display=swap">
<style>
:root{
  --blue:#0a6fc0;
  --blue-dark:#0c5fa6;
  --navy:#0e2740;
  --ink:#222;
  --muted:#555;
  --grey-bg:#f5f5f5;
  --white:#fff;
  --field:#3a8ad0;
}
*{margin:0;padding:0;box-sizing:border-box}
html,body{width:771px;height:1200px;overflow:hidden;background:var(--white);font-family:"Poppins",sans-serif;color:var(--ink)}
.page{position:relative;width:771px;height:1200px}
.abs{position:absolute}

/* header */
.brand{left:38px;top:14px;display:flex;align-items:center;gap:5px;font-family:"Poppins",sans-serif;font-weight:600;font-size:15px;color:var(--blue);letter-spacing:.2px}
.brand .mark{width:12px;height:12px;border:2px solid var(--blue)}
.nav{left:292px;top:19px;display:flex;gap:12px;font-size:7px;letter-spacing:.3px}
.nav a{color:var(--ink);text-decoration:none}
.nav a.active{color:var(--blue);position:relative}
.nav a.active::after{content:"^";position:absolute;left:7px;top:8px;font-size:8px}
.call{left:634px;top:15px;width:99px;height:24px;background:#120f26;display:flex;align-items:center}
.call .ic{width:24px;height:24px;background:var(--blue);display:flex;align-items:center;justify-content:center}
.call .txt{padding-left:10px;line-height:1}
.call .lbl{font-size:6px;color:#3c9be8}
.call .num{font-size:9px;color:var(--white);font-weight:500;margin-top:2px;white-space:nowrap}

/* hero */
.hero-art{left:0;top:0;width:771px;height:458px}
.hero-title-out{left:38px;top:158px;font-family:"Rajdhani",sans-serif;font-weight:500;font-size:46px;color:transparent;-webkit-text-stroke:1px var(--blue);letter-spacing:.5px;line-height:1}
.hero-title{left:37px;top:204px;font-family:"Rajdhani",sans-serif;font-weight:700;font-size:50px;color:var(--navy);line-height:1;letter-spacing:.3px}
.hero-tag{left:39px;top:258px;font-size:9.5px;color:var(--ink)}
.btn{display:flex;align-items:center;justify-content:center;background:var(--blue);color:var(--white);font-size:9.5px;font-weight:500;letter-spacing:.4px;height:27px;padding:0 10px;white-space:nowrap;line-height:1}
.btn-wrap{display:flex;align-items:center;gap:2px}
.slash{width:4px;height:27px;background:var(--blue);transform:skewX(-18deg)}
.hero-btn{left:39px;top:285px}
.slider-ctrl{left:38px;top:416px;display:flex;align-items:center;gap:5px}
.slider-ctrl .line{width:56px;height:1px;background:#999}
.slider-ctrl .b{width:21px;height:21px;border:1px solid #bbb;display:flex;align-items:center;justify-content:center}
.slider-ctrl .b.on{width:25px;height:25px;border-color:var(--blue)}

/* welcome */
.center{left:0;width:771px;text-align:center}
.eyebrow{top:505px;font-size:8.5px;color:var(--muted);letter-spacing:.3px}
.sec-title{font-size:19px;font-weight:500;color:var(--blue);letter-spacing:.5px}
.welcome-title{top:520px}
.copy{font-size:7.8px;color:var(--muted);line-height:12.5px}
.welcome-btn{left:341px;top:633px}

/* grants */
.grants{left:0;top:708px;width:771px;height:255px;background:linear-gradient(#f6f6f6 60%,#ececec)}
.grants-title{top:752px}
.grants-sub{top:787px}
.cards{left:101px;top:823px;display:flex;gap:9.5px}
.card{width:87px;height:100px;background:var(--white);box-shadow:0 2px 5px rgba(0,0,0,.06);text-align:center;padding-top:17px}
.card .icon{width:28px;height:28px;margin:0 auto 9px;border-radius:50%;background:var(--blue);opacity:.85}
.card .name{font-size:7.2px;line-height:10.5px;color:#222;letter-spacing:.2px}

/* footer */
.footer{left:0;top:963px;width:771px;height:237px;background:var(--blue)}
.foot-brand{left:52px;top:1009px;display:flex;align-items:center;gap:5px;font-weight:600;font-size:15px;color:var(--white)}
.foot-brand .mark{width:12px;height:12px;border:2px solid var(--white)}
.social{left:72px;top:1042px;display:flex;gap:4px}
.social span{width:22px;height:22px;border:1px solid var(--white)}
.f-head{top:990px;font-size:9.5px;color:var(--white);font-weight:500;letter-spacing:.4px}
.sitemap{left:213px;top:1020px;list-style:none;font-size:7.2px;color:var(--white)}
.sitemap li{height:14.5px;display:flex;align-items:center;gap:8px}
.sitemap li::before{content:"";width:3px;height:3px;border:1px solid var(--white)}
.ci{left:323px;display:flex;gap:12px;align-items:flex-start;color:var(--white)}
.ci .box{width:20px;height:19px;border:1px solid var(--white);display:flex;align-items:center;justify-content:center;flex:none}
.ci .t1{font-size:8.3px;white-space:nowrap}
.ci .t2{font-size:7px;margin-top:3px;white-space:nowrap}
.field{background:var(--field);color:#dfeefb;font-size:7px;padding:0 8px;display:flex;align-items:center}
.submit{left:515px;top:1116px;display:flex;align-items:center;gap:2px}
.submit .b{height:24px;padding:0 12px;border:1px solid var(--white);color:var(--white);font-size:9.5px;display:flex;align-items:center;white-space:nowrap}
.submit .s{width:3px;height:24px;background:var(--white);transform:skewX(-18deg)}
.rule{left:38px;top:1169px;width:695px;height:1px;background:rgba(255,255,255,.25)}
.copyright{top:1178px;font-size:7.3px;color:var(--white)}
</style>
</head>
<body>
<div class="page">

  <svg class="abs hero-art" viewBox="0 0 771 458" role="img" aria-label="Glowing x-ray style illustration of a human skeleton with a highlighted brain">
    <defs>
      <radialGradient id="glow" cx="0.65" cy="0.3" r="0.7">
        <stop offset="0" stop-color="#d9506a"/>
        <stop offset="0.3" stop-color="#3a7fb0"/>
        <stop offset="0.7" stop-color="#1d1a4a"/>
        <stop offset="1" stop-color="#120d2a"/>
      </radialGradient>
    </defs>
    <polygon points="464,0 771,0 771,458 442,458 291,212" fill="url(#glow)"/>
    <polygon points="347,344 358,344 432,457 420,457" fill="var(--blue)"/>
  </svg>

  <div class="abs brand"><span class="mark"></span>CORWENNA</div>
  <nav class="abs nav">
    <a class="active">HOME</a><a>ABOUT</a><a>GRANTS</a><a>CONTACT</a>
  </nav>
  <div class="abs call">
    <div class="ic"><svg width="12" height="12" viewBox="0 0 24 24"><path fill="#fff" d="M6.6 10.8a15 15 0 0 0 6.6 6.6l2.2-2.2c.3-.3.7-.4 1-.2 1.1.4 2.3.6 3.6.6.6 0 1 .4 1 1V20c0 .6-.4 1-1 1A17 17 0 0 1 3 4c0-.6.4-1 1-1h3.5c.6 0 1 .4 1 1 0 1.3.2 2.5.6 3.6.1.3 0 .7-.2 1z"/></svg></div>
    <div class="txt"><div class="lbl">Call Us On :</div><div class="num">0123 555 0190</div></div>
  </div>

  <div class="abs hero-title-out">CORWENNA</div>
  <div class="abs hero-title">FOUNDATION</div>
  <div class="abs hero-tag">Reduce The Suffering Caused By Chronic Pain.</div>
  <div class="abs hero-btn btn-wrap"><span class="btn">CONTACT US</span><span class="slash"></span></div>
  <div class="abs slider-ctrl">
    <span class="line"></span>
    <span class="b"><svg width="8" height="10" viewBox="0 0 8 10"><path d="M6 1 2 5l4 4" fill="none" stroke="#999" stroke-width="1"/></svg></span>
    <span class="b on"><svg width="8" height="10" viewBox="0 0 8 10"><path d="M2 1l4 4-4 4" fill="none" stroke="#0a6fc0" stroke-width="1.3"/></svg></span>
  </div>

  <div class="abs center eyebrow">WELCOME TO</div>
  <h1 class="abs center sec-title welcome-title">CORWENNA FOUNDATION</h1>
  <p class="abs center copy" style="top:553px">Corwenna Foundation is a grant making charity set up in the UK in 2021</p>
  <p class="abs center copy" style="top:573px">The main aim of Corwenna Foundation is to reduce the suffering caused<br>by chronic pain.</p>
  <p class="abs center copy" style="top:607px">Charity registration number 1187654.</p>
  <div class="abs welcome-btn btn-wrap"><span class="btn" style="padding:0 13px">ABOUT US</span><span class="slash"></span></div>

  <section class="abs grants"></section>
  <h2 class="abs center sec-title grants-title">GRANTS</h2>
  <p class="abs center copy grants-sub">The Main Categories of Funding for Pain Research or Education will Be as Follows.</p>
  <div class="abs cards">
    <div class="card"><div class="icon" role="img" aria-label="Head with pain icon"></div><div class="name">PAIN<br>CENTRES</div></div>
    <div class="card"><div class="icon" role="img" aria-label="Medicine bottle icon"></div><div class="name">THE USE OF<br>OPIOIDS</div></div>
    <div class="card"><div class="icon" role="img" aria-label="Pill icon"></div><div class="name">IMPROVING<br>THE USE OF<br>MEDICATION</div></div>
    <div class="card"><div class="icon" role="img" aria-label="Graduation cap icon"></div><div class="name">EDUCATION</div></div>
    <div class="card"><div class="icon" role="img" aria-label="Head with target icon"></div><div class="name">IMPROVED<br>TYPES OF PAIN<br>CONTROL</div></div>
    <div class="card"><div class="icon" role="img" aria-label="Body with back pain icon"></div><div class="name">MEASURING<br>PAIN</div></div>
  </div>

  <footer class="abs footer"></footer>
  <div class="abs foot-brand"><span class="mark"></span>CORWENNA</div>
  <div class="abs social"><span></span><span></span><span></span></div>

  <div class="abs f-head" style="left:212px">SITEMAP</div>
  <ul class="abs sitemap"><li>Home</li><li>About</li><li>Grants</li><li>Contact</li></ul>

  <div class="abs f-head" style="left:324px">CONTACT US</div>
  <div class="abs ci" style="top:1021px">
    <span class="box"><svg width="10" height="12" viewBox="0 0 10 12"><path d="M5 11S1 6.5 1 4a4 4 0 0 1 8 0c0 2.5-4 7-4 7z" fill="none" stroke="#fff"/><circle cx="5" cy="4" r="1.4" fill="#fff"/></svg></span>
    <div><div class="t1">Corwenna Foundation</div><div class="t2">101 - lorem ipsum simple text</div></div>
  </div>
  <div class="abs ci" style="top:1050px">
    <span class="box"><svg width="11" height="11" viewBox="0 0 24 24"><path fill="#fff" d="M6.6 10.8a15 15 0 0 0 6.6 6.6l2.2-2.2c.3-.3.7-.4 1-.2 1.1.4 2.3.6 3.6.6.6 0 1 .4 1 1V20c0 .6-.4 1-1 1A17 17 0 0 1 3 4c0-.6.4-1 1-1h3.5c.6 0 1 .4 1 1 0 1.3.2 2.5.6 3.6.1.3 0 .7-.2 1z"/></svg></span>
    <div class="t1" style="padding-top:4px">0123 555 0190</div>
  </div>
  <div class="abs ci" style="top:1076px">
    <span class="box"><svg width="11" height="8" viewBox="0 0 11 8"><rect width="11" height="8" rx="1" fill="#fff"/><path d="M0 1l5.5 3.5L11 1" fill="none" stroke="#0a6fc0"/></svg></span>
    <div class="t2" style="padding-top:5px">info@corwennafoundation.org</div>
  </div>

  <div class="abs f-head" style="left:515px">GET IN TOUCH</div>
  <div class="abs field" style="left:515px;top:1021px;width:106px;height:22px">Name *</div>
  <div class="abs field" style="left:626px;top:1021px;width:106px;height:22px">Phone *</div>
  <div class="abs field" style="left:515px;top:1048px;width:106px;height:22px">Email *</div>
  <div class="abs field" style="left:626px;top:1048px;width:106px;height:22px">Services *</div>
  <div class="abs field" style="left:515px;top:1075px;width:217px;height:38px;align-items:flex-start;padding-top:5px">Message *</div>
  <div class="abs submit"><span class="b">SUBMIT</span><span class="s"></span></div>

  <div class="abs rule"></div>
  <div class="abs center copyright">©Corwenna Foundation - 2021 All rights reserved.</div>
</div>
</body>
</html>
```